Medical Prescription for Diagnostic Sleep Testing

Tamber Ridge Vital Labs main marketing tool is our Prescription that we leave with medical providers. Prescription is printed on 8.5 x 11 sheets of paper to create a prescription pad for our medical providers. Prescription should fit to one page. Tamber Ridge Vital Labs works with 250 different medical providers so it is important we are able to update and change the medical provider information at bottom. The medical provider would fill-out top with patient information, check-off center testing and patient co-morbidity and Fax to Tamber Ridge Vital Labs. Because it is Faxed to us it is important to have clear print and large font Attached or uploaded file is one example we currently use. Please review all 5 must haves.

Target Market(s)

Prescription for medical providers to fill-out and fax to Tamber Ridge Vital Labs to conduct the sleep study.

Industry/Entity Type

Medical

Colors

Designer to choose only greyscale colors for use in the design.

Requirements
Must have
• 1) Prescription Size: 8.5 x 11
• 2) Must fit to One page Only
• 3) Ability to change medical provider information at bottom of prescription. We work with 250 different medical providers
• 4) Ability to change or update any part of prescription
• 5) Document Must be created in Microsoft Word 2016. This is the program we use for our prescriptions.
Nice to have
• Can be done in Gray-Scale or Black and White since its being faxed from the medical provider to us.

```html
<!DOCTYPE html>
<html lang="en">
<head>
<meta charset="utf-8">
<title>Sleep Study Physician Order</title>
<link href="https://fonts.googleapis.com/css2?family=Oswald:wght@500;600&family=Lato:wght@400;700&family=Tinos&display=swap" rel="stylesheet">
<style>
:root{
  --ink:#333333;
  --dark:#333333;
  --text:#222222;
  --panel:#e9ecef;
  --paper:#ffffff;
  --backdrop:#e4e4e4;
  --box:#8a8a8a;
}
*{box-sizing:border-box;margin:0;padding:0}
html,body{width:1200px;height:1200px;overflow:hidden;background:var(--backdrop)}
.sheet{position:absolute;left:133px;top:0;width:1032px;height:1326px;background:var(--paper);transform:scale(.905);transform-origin:0 0;font-family:'Lato',sans-serif;color:var(--text)}
.abs{position:absolute}
.header{left:0;top:0;width:1032px;height:157px}
.brand{left:62px;top:24px;width:212px;height:118px;border:2px solid var(--ink);border-radius:6px;display:flex;flex-direction:column;align-items:center;justify-content:center;gap:10px}
.brand-name{font-family:'Lato',sans-serif;font-weight:700;font-size:21px;line-height:1.15;color:var(--ink);text-align:center}
.badge{width:60px;height:14px;background:#bdbdbd;border-radius:2px}
.title{left:367px;top:22px;font-family:'Oswald',sans-serif;font-weight:600;font-size:47px;color:#fff;letter-spacing:.3px;line-height:1}
.contact{color:#fff;font-size:20px;display:flex;align-items:center;gap:14px}
.contact svg{width:18px;height:20px;fill:#fff;flex:none}
.field{font-family:'Tinos',serif;font-size:17px;color:var(--text);display:flex;align-items:flex-end;white-space:nowrap}
.field .line{border-bottom:1px solid #333;height:16px;margin-left:2px}
.bar{left:29px;width:974px;background:var(--dark);color:#fff;font-family:'Oswald',sans-serif;font-weight:500;text-align:center}
.cb{display:inline-block;width:17px;height:17px;border:1.5px solid var(--box);background:#fff;flex:none}
.test{left:42px;display:flex;gap:14px;font-size:16px;line-height:22px}
.test b{font-weight:700}
.panel{left:29px;width:974px;background:var(--panel)}
.cond{display:flex;gap:14px;font-size:16px;height:26px;align-items:center}
.cond.indent{padding-left:31px}
.col{top:778px;display:flex;flex-direction:column}
.clinic-name{font-family:'Oswald',sans-serif;font-weight:600;font-size:27px;color:var(--ink);line-height:1}
.clinic{font-size:16px;line-height:24px}
.doc{display:flex;gap:14px}
.doc-name{font-family:'Oswald',sans-serif;font-weight:500;font-size:15px;line-height:18px}
.doc-npi{font-size:12.5px;line-height:18px}
.footer{left:0;top:1215px;width:1032px;height:111px;background:var(--dark);color:#fff;text-align:center}
</style>
</head>
<body>
<div class="sheet">
  <svg class="abs header" viewBox="0 0 1032 157" aria-hidden="true"><polygon points="345,0 1032,0 1032,157 290,157" fill="#333"/></svg>
  <div class="abs brand"><div class="brand-name">Tamber Ridge<br>Vital Labs</div><div class="badge"></div></div>
  <div class="abs title">SLEEP STUDY PHYSICIAN ORDER</div>
  <div class="abs contact" style="left:372px;top:86px"><svg viewBox="0 0 24 24"><path d="M6.6 2.5l3 3.5-2 2.3c1.2 2.8 3.3 5 6.1 6.3l2.2-2 3.6 3-1.8 3.2C10 18.5 5.3 13.4 4 5z"/></svg>(702) 555-0162</div>
  <div class="abs contact" style="left:372px;top:122px"><svg viewBox="0 0 24 24"><rect x="3" y="8" width="18" height="13" rx="1.5"/><rect x="7" y="3" width="10" height="6" fill="#fff" stroke="#fff"/><rect x="6" y="11" width="12" height="2" fill="#333"/><rect x="6" y="15" width="3" height="2" fill="#333"/><rect x="11" y="15" width="3" height="2" fill="#333"/></svg>(702) 555-0168</div>
  <div class="abs contact" style="left:702px;top:86px;align-items:flex-start"><svg viewBox="0 0 24 24" style="margin-top:3px"><path d="M12 2a7 7 0 0 0-7 7c0 5 7 13 7 13s7-8 7-13a7 7 0 0 0-7-7zm0 9.5a2.5 2.5 0 1 1 0-5 2.5 2.5 0 0 1 0 5z"/></svg><span style="line-height:30px">2480 W. Mesa Vista Drive,<br>Suite 7-C; Las Vegas, NV 89120</span></div>

  <div class="abs field" style="left:30px;top:172px">Patient Name:<span class="line" style="width:512px"></span><span style="margin-left:26px">DOB: <span class="line" style="display:inline-block;width:90px"></span>/<span class="line" style="display:inline-block;width:92px"></span>/<span class="line" style="display:inline-block;width:92px"></span></span></div>
  <div class="abs field" style="left:32px;top:214px">Telephone: <span class="line" style="width:424px;margin-left:6px"></span><span style="margin-left:30px">Alternate Telephone:</span><span class="line" style="width:280px"></span></div>
  <div class="abs field" style="left:30px;top:257px">Primary Insurance: <span class="line" style="width:360px;margin-left:6px"></span><span style="margin-left:32px">Secondary Insurance:</span><span class="line" style="width:278px"></span></div>
  <div class="abs field" style="left:30px;top:299px">Height:<span class="line" style="width:262px"></span><span style="margin-left:20px">Weight:</span><span class="line" style="width:288px"></span><span style="margin-left:20px">Patient Gender (circle one): &nbsp; M &nbsp; / &nbsp; F</span></div>

  <div class="abs bar" style="top:343px;height:42px;font-size:27px;line-height:42px">DIAGNOSTIC SLEEP STUDY ORDERED</div>

  <div class="abs test" style="top:403px"><span class="cb" style="margin-top:3px"></span><div><b>COMPLETE SLEEP STUDY:</b>&nbsp; (Based on Insurance or Patient’s Choice)<div style="padding-left:206px;margin-top:5px">In-Lab Sleep Study (PSG) or Home Sleep Study (PSG 95810 / HST 95806)<br>with follow-up PAP Titration Study (PAP 95811 if positive for sleep apnea)</div></div></div>
  <div class="abs test" style="top:488px"><span class="cb" style="margin-top:3px"></span><div><b>PEDIATRIC SLEEP STUDY:</b>&nbsp; PSG w/End Tidal CO2 Monitoring<div style="padding-left:194px;margin-top:3px">(PSG 95782 under 6 years of age &amp; PSG 95810 older than 6 years of age)</div></div></div>
  <div class="abs test" style="top:547px"><span class="cb" style="margin-top:3px"></span><div>In-Lab Diagnostic Sleep Study/Polysomnogram (PSG 95810)</div></div>
  <div class="abs test" style="top:584px;width:900px"><span class="cb" style="margin-top:3px"></span><div style="line-height:20px">SPLIT-NIGHT STUDY (PSG with PAP 95810 &amp; 95811)<br><b style="text-decoration:underline">To Comply With Accreditation &amp; Insurance Guidelines:</b>&nbsp; AHI must be 20 or greater with minimum 2 hour recorded sleep time and 3 hours minimum to complete PAP treatment.</div></div>
  <div class="abs test" style="top:659px"><span class="cb" style="margin-top:3px"></span><div>CPAP/BiPAP/BiPAP ST Titration Study (Patients with documented sleep apnea 95811)</div></div>
  <div class="abs test" style="top:691px"><span class="cb" style="margin-top:3px"></span><div>Home Sleep Study (HST 95806 Conducted in patient’s home &amp; unattended by technologist) (No insurance patient cost $250.00)</div></div>

  <div class="abs bar" style="top:734px;height:36px;font-size:21px;line-height:36px">PATIENT MEDICAL NECESSITY – PLEASE CHECK ALL BOXES THAT APPLY</div>
  <div class="abs panel" style="top:770px;height:252px"></div>
  <div class="abs col" style="left:42px">
    <div class="cond"><span class="cb"></span>Atrial Fibrillation</div>
    <div class="cond"><span class="cb"></span>Bipolar Disorder</div>
    <div class="cond"><span class="cb"></span>Congestive Heart Failure</div>
    <div class="cond"><span class="cb"></span>COPD</div>
    <div class="cond"><span class="cb"></span>Depression</div>
    <div class="cond"><span class="cb"></span>Excessive Daytime Sleepiness</div>
    <div class="cond"><span class="cb"></span>Gasping Sensations with</div>
    <div class="cond indent">Frequent Awakenings</div>
    <div class="cond"><span class="cb"></span>Frequent Urination</div>
  </div>
  <div class="abs col" style="left:390px">
    <div class="cond"><span class="cb"></span>Heart Disease</div>
    <div class="cond"><span class="cb"></span>History Heart Attack</div>
    <div class="cond"><span class="cb"></span>Hypertension</div>
    <div class="cond"><span class="cb"></span>Insomnia</div>
    <div class="cond"><span class="cb"></span>Mental or Mood Disorder</div>
    <div class="cond"><span class="cb"></span>Loud Snoring</div>
    <div class="cond"><span class="cb"></span>Morbid Obesity / Obesity</div>
    <div class="cond"><span class="cb"></span>Morning Headaches</div>
    <div class="cond"><span class="cb"></span>Narcolepsy</div>
  </div>
  <div class="abs col" style="left:716px">
    <div class="cond"><span class="cb"></span>Opioid Use</div>
    <div class="cond"><span class="cb"></span>PTSD</div>
    <div class="cond"><span class="cb"></span>Pulmonary Disease</div>
    <div class="cond"><span class="cb"></span>Restless Leg Syndrome</div>
    <div class="cond"><span class="cb"></span>Seizures</div>
    <div class="cond"><span class="cb"></span>Shift Work Sleep disorder</div>
    <div class="cond"><span class="cb"></span>Stroke / TIA</div>
    <div class="cond"><span class="cb"></span>Witnessed Apnea</div>
    <div class="cond"><span class="cb"></span>Other:<span style="display:inline-block;width:200px;border-bottom:1px solid #333;height:16px;margin-left:-12px"></span></div>
  </div>

  <div class="abs panel" style="top:1036px;height:117px"></div>
  <div class="abs" style="left:42px;top:1044px">
    <div class="clinic-name">SIERRA CREST EAR + SINUS</div>
    <div class="clinic" style="margin-top:6px">5120 N. Canyon Road; Las Vegas, NV 89121-4410</div>
    <div class="clinic"><b>Telephone:</b>&nbsp; 702-555-0147</div>
    <div class="clinic"><b>Fax:</b>&nbsp; 702-555-0193</div>
  </div>
  <div class="abs doc" style="left:418px;top:1048px"><span class="cb"></span><div><div class="doc-name">Dr. Martin Alvarez Reyes</div><div class="doc-npi">NPI: 1730264815</div></div></div>
  <div class="abs doc" style="left:615px;top:1048px"><span class="cb"></span><div><div class="doc-name">Dr. Paul R. Hensley</div><div class="doc-npi">NPI: 1480573926</div></div></div>
  <div class="abs doc" style="left:815px;top:1048px"><span class="cb"></span><div><div class="doc-name" style="font-size:13.5px">Dr. Leonard K. Brzezinski</div><div class="doc-npi">NPI: 1902648371</div></div></div>
  <div class="abs doc" style="left:418px;top:1106px"><span class="cb"></span><div><div class="doc-name">Dr. Grace Lum</div><div class="doc-npi">NPI: 1264830957</div></div></div>
  <div class="abs doc" style="left:615px;top:1106px"><span class="cb"></span><div><div class="doc-name">Nora Beltran, FNP-C</div><div class="doc-npi">NPI: 1578209364</div></div></div>
  <div class="abs doc" style="left:815px;top:1106px"><span class="cb"></span><div><div class="doc-name">Evan Pruitt, PA-C</div><div class="doc-npi">NPI: 1345926078</div></div></div>

  <div class="abs field" style="left:29px;top:1172px">Physician’s Signature:<span class="line" style="width:548px"></span><span style="margin-left:18px">Date: <span class="line" style="display:inline-block;width:62px"></span>/<span class="line" style="display:inline-block;width:64px"></span>/<span class="line" style="display:inline-block;width:62px"></span></span></div>

  <div class="abs footer">
    <div style="font-weight:700;font-size:22px;margin-top:10px">Please Fax: 702-555-0168 or Email: info@tamberridgevitallabs.com</div>
    <div style="font-size:18px;margin-top:5px;display:flex;justify-content:center;align-items:center;gap:12px"><svg width="20" height="18" viewBox="0 0 20 18" aria-hidden="true"><rect x="1" y="3" width="13" height="13" fill="none" stroke="#fff" stroke-width="1.6"/><path d="M4 9l4 4 10-12" fill="none" stroke="#fff" stroke-width="2.2"/></svg>Fax Along With: Patient Demographic Information &nbsp;•&nbsp; Copy of Current Insurance Information &nbsp;•&nbsp; Clinical Notes</div>
    <div style="font-size:17px;margin-top:4px">Thank You For your support MARCO &amp; LEE</div>
  </div>
</div>
</body>
</html>
```